website design for B&T Electric

A portfolio website for a high end commercial and residential electrical contracting company. The current site bandtelectric.example does not represent the current direction but the images in the gallery give you an idea of the work we do. Current logo will be uploaded shortly but is black text on white background.
Target Market(s)
General Contractors, Residential Home Owners, clients intersted in Voskal home automation.
Industry/Entity Type
Electrician
Coding
Coded - Design and coding required
Number of Pages Required
2 page
Font styles to use
Sans Serif
Colors
Designer to choose colors to be used in the design.
Requirements
Must have
- Portfolio section highlighting different service areas and products (Voskal Dwellsync, etc)

```html
<!DOCTYPE html>
<html lang="en">
<head>
<meta charset="utf-8">
<title>B&amp;T Electric</title>
<link href="https://fonts.googleapis.com/css2?family=Jost:wght@400;500;700&display=swap" rel="stylesheet">
<style>
:root{
  --ink:#111;
  --blue:#0b4ea2;
  --blue-dark:#0a3f85;
  --grey-bg:#ececec;
  --panel:#f4f4f4;
  --line:#d8d8d8;
  --muted:#8a8a8a;
  --footer:#111;
  --white:#fff;
}
*{box-sizing:border-box;margin:0;padding:0}
html,body{width:960px;height:1200px;overflow:hidden;background:var(--white)}
body{font-family:"Jost",sans-serif;color:var(--ink);position:relative}
.site-header{position:absolute;left:0;top:0;width:960px;height:79px;background:var(--white)}
.brand{position:absolute;left:12px;top:22px;font-size:29px;font-weight:700;letter-spacing:.5px;color:var(--ink)}
.main-nav{position:absolute;right:70px;top:31px;display:flex;gap:23px;font-size:14px;font-weight:500}
.main-nav a{color:var(--ink);text-decoration:none;text-transform:uppercase}
.main-nav a.active{color:var(--blue);border-bottom:2px solid var(--blue);padding-bottom:3px}
.search-icon{position:absolute;right:24px;top:32px}
.hero{position:absolute;left:0;top:79px;width:960px;height:339px;background:linear-gradient(90deg,#4a2418 0%,#7a3a22 40%,#6a3020 70%,#3a1c12 100%)}
.hero-caption{position:absolute;left:274px;top:80px;width:412px;height:195px;background:rgba(20,20,25,.55);text-align:center;color:var(--white)}
.hero-caption h1{font-size:21px;font-weight:500;letter-spacing:1px;margin-top:25px}
.hero-caption p{font-size:12px;line-height:19px;margin:16px 30px 0;letter-spacing:.3px}
.btn-more{display:inline-block;margin-top:14px;background:var(--blue);color:var(--white);font-size:14px;font-weight:500;padding:6px 22px;border-radius:3px}
.hero-arrow{position:absolute;top:145px;width:46px;height:46px;border-radius:50%;background:rgba(0,0,0,.75)}
.hero-arrow.prev{left:12px}.hero-arrow.next{right:14px}
.services{position:absolute;left:0;top:418px;width:960px;height:423px;background:var(--grey-bg)}
.section-title{position:absolute;left:0;width:960px;top:28px;text-align:center;font-size:19px;font-weight:500}
.title-rule{position:absolute;left:416px;top:56px}
.tile{position:absolute;width:223px;height:140px;overflow:hidden}
.tile-name{position:absolute;left:15px;bottom:10px;color:var(--white);font-size:21px;text-shadow:0 1px 3px rgba(0,0,0,.6)}
.tile-icon{position:absolute;left:16px;top:0;width:41px;height:41px;background:var(--blue);display:flex;align-items:center;justify-content:center}
.zoom{position:absolute;right:16px;bottom:12px}
.testimonials{position:absolute;left:12px;top:870px;width:456px}
.testimonials h2{font-size:20px;font-weight:400}
.slider-btn{position:absolute;top:4px;width:29px;height:24px;border:1px solid var(--line);background:var(--white);display:flex;align-items:center;justify-content:center}
.quote-card{position:absolute;left:12px;top:904px;width:456px;height:225px;background:var(--panel);border:1px solid var(--line);border-left:3px solid var(--blue)}
.avatar{position:absolute;left:26px;top:25px;width:82px;height:82px;border-radius:50%;border:3px solid var(--blue-dark);background:linear-gradient(#b9a89a,#6f5d52)}
.quote-name{position:absolute;left:152px;top:58px;font-size:15px;text-transform:uppercase}
.quote-text{position:absolute;left:26px;top:130px;width:420px;font-size:13px;line-height:17.5px}
.contact-card{position:absolute;left:490px;top:904px;width:457px;height:225px;background:var(--panel);border:1px solid var(--line)}
.contact-card h2{position:absolute;left:0;width:100%;top:36px;text-align:center;font-size:20px;font-weight:400;color:#0d2c55}
.field{position:absolute;font-size:12px;color:var(--muted);border-bottom:1px solid #cfcfcf;padding-bottom:7px}
.send{position:absolute;right:24px;top:172px;display:flex;align-items:center;gap:8px;font-size:15px}
.site-footer{position:absolute;left:0;top:1161px;width:960px;height:39px;background:var(--footer);color:var(--white)}
.site-footer small{position:absolute;left:12px;top:12px;font-size:11px}
.social{position:absolute;top:9px;width:22px;height:22px;border-radius:50%}
</style>
</head>
<body>
<header class="site-header">
  <div class="brand">B&amp;T ELECTRIC</div>
  <nav class="main-nav">
    <a class="active">Home</a><a>Gallery</a><a>Specialty Services</a><a>About</a><a>Contact</a>
  </nav>
  <svg class="search-icon" width="15" height="15" viewBox="0 0 15 15"><circle cx="6" cy="6" r="4.5" fill="none" stroke="#111" stroke-width="2"/><line x1="9.5" y1="9.5" x2="14" y2="14" stroke="#111" stroke-width="2.5"/></svg>
</header>

<section class="hero" role="img" aria-label="Warmly lit classic living room interior">
  <div class="hero-caption">
    <h1>RESIDENTIAL</h1>
    <p>Lorem Ipsum is simply dummy text of the printing and typesetting industry. Lorem Ipsum has been the industry's standard dummy text ever since the 1500s, a type specimen book.</p>
    <span class="btn-more">MORE</span>
  </div>
  <div class="hero-arrow prev"><svg width="46" height="46"><polyline points="26,13 16,23 26,33" fill="none" stroke="#fff" stroke-width="1.5"/></svg></div>
  <div class="hero-arrow next"><svg width="46" height="46"><polyline points="20,13 30,23 20,33" fill="none" stroke="#fff" stroke-width="1.5"/></svg></div>
</section>

<section class="services">
  <h2 class="section-title">Home</h2>
  <svg class="title-rule" width="128" height="20" viewBox="0 0 128 20"><line x1="0" y1="10" x2="56" y2="10" stroke="#111"/><line x1="72" y1="10" x2="128" y2="10" stroke="#111"/><polygon points="66,1 59,11 64,11 61,19 69,8 64,8" fill="#111"/></svg>

  <div class="tile" style="left:12px;top:93px;background:linear-gradient(#1f2a3a,#3a3a40)" role="img" aria-label="Commercial building at dusk">
    <div class="tile-icon"><svg width="22" height="22"><rect x="3" y="6" width="16" height="14" fill="none" stroke="#fff" stroke-width="2"/><rect x="8" y="2" width="6" height="5" fill="#fff"/></svg></div>
    <span class="tile-name">Commercial</span>
    <svg class="zoom" width="20" height="20"><circle cx="8" cy="8" r="6.5" fill="none" stroke="#fff" stroke-width="1.3"/><line x1="13" y1="13" x2="19" y2="19" stroke="#fff" stroke-width="1.5"/><line x1="5" y1="8" x2="11" y2="8" stroke="#fff"/><line x1="8" y1="5" x2="8" y2="11" stroke="#fff"/></svg>
  </div>
  <div class="tile" style="left:250px;top:93px;background:linear-gradient(135deg,#6a3a18,#c07a35,#4a2810)" role="img" aria-label="Wood-paneled library with lit shelves">
    <div class="tile-icon"><svg width="22" height="22"><polygon points="11,2 2,11 5,11 5,20 17,20 17,11 20,11" fill="#fff"/></svg></div>
    <span class="tile-name">Residential</span>
  </div>
  <div class="tile" style="left:487px;top:93px;background:linear-gradient(#0c1a3a,#3a2a20 70%,#6a4020)" role="img" aria-label="Home exterior with landscape lighting at night">
    <div class="tile-icon"><svg width="24" height="22"><polygon points="1,17 8,9 13,13 17,10 23,17" fill="#fff"/><circle cx="6" cy="7" r="2" fill="#fff"/></svg></div>
    <span class="tile-name">Landscape</span>
  </div>
  <div class="tile" style="left:722px;top:93px;width:225px;background:linear-gradient(135deg,#fafafa,#d4d6d8)" role="img" aria-label="Standby home generator unit">
    <div class="tile-icon"><svg width="24" height="20"><rect x="2" y="5" width="20" height="12" fill="none" stroke="#fff" stroke-width="2"/><rect x="5" y="9" width="6" height="4" fill="#fff"/></svg></div>
    <span class="tile-name">Generators</span>
  </div>

  <div class="tile" style="left:12px;top:247px;background:linear-gradient(#5a6a80,#3a3028)" role="img" aria-label="Living room with motorized window shades">
    <div class="tile-icon"><svg width="24" height="22"><rect x="2" y="3" width="16" height="12" fill="none" stroke="#fff" stroke-width="2"/><line x1="2" y1="8" x2="18" y2="8" stroke="#fff" stroke-width="2"/><line x1="19" y1="10" x2="19" y2="20" stroke="#fff" stroke-width="2"/></svg></div>
    <span class="tile-name">Voskal Shades</span>
  </div>
  <div class="tile" style="left:250px;top:247px;background:linear-gradient(135deg,#d9b890,#a8825a)" role="img" aria-label="Wall-mounted lighting keypad">
    <div class="tile-icon"><svg width="24" height="24"><circle cx="12" cy="12" r="10" fill="#fff"/></svg></div>
    <span class="tile-name">Voskal Dimming</span>
  </div>
  <div class="tile" style="left:487px;top:247px;background:linear-gradient(135deg,#1e3e70,#8aa8c8,#2a4a78)" role="img" aria-label="Pile of LED light bulbs">
    <div class="tile-icon"><svg width="20" height="24"><rect x="6" y="7" width="8" height="11" rx="3" fill="none" stroke="#fff" stroke-width="2"/><line x1="7" y1="21" x2="13" y2="21" stroke="#fff" stroke-width="2"/><line x1="10" y1="1" x2="10" y2="4" stroke="#fff" stroke-width="1.5"/><line x1="3" y1="3" x2="5" y2="5" stroke="#fff" stroke-width="1.5"/><line x1="17" y1="3" x2="15" y2="5" stroke="#fff" stroke-width="1.5"/></svg></div>
    <span class="tile-name">Led Lighting</span>
  </div>
  <div class="tile" style="left:722px;top:247px;width:225px;background:linear-gradient(135deg,#e8d8cc,#f0ece8,#c8ccd8)" role="img" aria-label="Customer service staff on headsets">
    <div class="tile-icon"><svg width="24" height="24"><path d="M4 14 V11 A8 8 0 0 1 20 11 V14" fill="none" stroke="#fff" stroke-width="2"/><rect x="2" y="12" width="4" height="7" rx="1.5" fill="#fff"/><rect x="18" y="12" width="4" height="7" rx="1.5" fill="#fff"/><circle cx="12" cy="13" r="4" fill="#fff"/></svg></div>
    <span class="tile-name">Services Calls</span>
  </div>
</section>

<div class="testimonials">
  <h2>TESTIMONIALS</h2>
  <span class="slider-btn" style="left:393px"><svg width="10" height="12"><polyline points="7,1 2,6 7,11" fill="none" stroke="#111"/></svg></span>
  <span class="slider-btn" style="left:427px"><svg width="10" height="12"><polyline points="3,1 8,6 3,11" fill="none" stroke="#111"/></svg></span>
</div>
<article class="quote-card">
  <div class="avatar" role="img" aria-label="Client portrait"></div>
  <div class="quote-name">Dane Harlow</div>
  <p class="quote-text">Lorem Ipsum is simply dummy text of the printing and typesetting industry. Lorem Ipsum has been the industry's standard dummy text ever since the 1500s, when an unknown printer took a galley of type and scrambled it to make a type specimen book.</p>
</article>

<section class="contact-card">
  <h2>GET IN TOUCH</h2>
  <div class="field" style="left:21px;top:86px;width:198px">Name</div>
  <div class="field" style="left:235px;top:86px;width:198px">Email</div>
  <div class="field" style="left:21px;top:127px;width:412px">Message</div>
  <div class="send"><svg width="22" height="16"><rect x="1" y="1" width="20" height="14" fill="none" stroke="#0b4ea2" stroke-width="1.5"/><polyline points="1,1 11,9 21,1" fill="none" stroke="#0b4ea2" stroke-width="1.5"/></svg>Send message</div>
</section>

<footer class="site-footer">
  <small>© 2017 All rights reserved.</small>
  <span class="social" style="left:860px;background:#4aa3df" aria-label="Social link"></span>
  <span class="social" style="left:892px;background:#3b5998" aria-label="Social link"></span>
  <span class="social" style="left:925px;background:#d33a3a" aria-label="Social link"></span>
</footer>
</body>
</html>
```